Education, Principal Business Card

I would like a double-sided, full colour business card for my personal use as Principal of a Primary School. The card needs to feature the school logo (.jpeg and .eps files attached), along with the following details:

Gareth Moffat
PRINCIPAL
Pelbrook Primary School
117 Carrisfield Road HIGH WYCOMBE WA 6148
t: (08) 9371 2654 f: (08) 9371 5902 m: 0438 592 706
e: Gareth.Moffat@learnmail-west.example
w: www.pelbrookps.example.edu
l: au.proflink.example/in/garethmoffat/

The arrangement of details between front and back of the card is at your discretion as are fonts. Colours limited to black, red and white. Looking for bold and modern / clean design in a print-ready publication.

Target Market(s)

Parents, colleagues, professionals.

Industry/Entity Type

School

Contact Information for Business Card

As per project brief.

Font styles to use
Serif
Sans Serif
Decorative
Script

Colors
ea1f26
ffffff
000000

Requirements
Must have
• All of the listed contact details. Strong feature of the school logo and corporate colours of black, red and white.
Nice to have
• Rounded corners design a plus. If all details could be placed on the front, a bold education themed quote on the reverse side of the card would be great. Suggested quotes;
• “Education is the most powerful weapon which you can use to change the world.”
• ― Tobias Ferrante
• "Be who you are
• and say what you feel
• because those who mind don't matter
• and those who matter don't mind." Dr Plimm
Should not have
• Clip art, Times New Roman, Arial or boring fonts, low resolution image (please use the vector file if possible).

```html
<!DOCTYPE html>
<html lang="en">
<head>
<meta charset="utf-8">
<title>Gareth Moffat – Principal Business Card</title>
<link rel="stylesheet" href="https://fonts.googleapis.com/css2?family=Roboto+Condensed:wght@400;700&family=Federant&family=Black+Ops+One&family=Archivo+Black&family=Oswald:wght@500&family=Playfair+Display:ital,wght@1,700&display=swap">
<style>
:root{
  --page:#ececec;
  --red:#ea1f26;
  --ink:#2a2a2a;
  --charcoal:#2c2c2c;
  --white:#ffffff;
  --back-grey:#e4e4e4;
}
*{box-sizing:border-box;margin:0;padding:0}
html,body{width:963px;height:1200px;overflow:hidden;background:var(--page)}
.canvas{position:relative;width:963px;height:1200px}
.card{position:absolute;border-radius:28px;overflow:hidden;box-shadow:0 6px 14px rgba(0,0,0,.28)}

/* front */
.card-front{left:118px;top:88px;width:724px;height:455px;background:var(--white)}
.front-shapes{position:absolute;inset:0}
.school-name{position:absolute;left:25px;top:120px;width:200px;text-align:center;
  font-family:"Roboto Condensed",sans-serif;font-weight:700;color:var(--ink);text-transform:uppercase}
.school-dot{display:block;width:70px;height:70px;border-radius:50%;background:var(--red);margin:0 auto 14px}
.school-name .line1{display:block;font-size:30px;line-height:32px;letter-spacing:3px}
.school-name .line2{display:block;font-size:17px;line-height:20px;letter-spacing:.5px}
.identity{position:absolute;right:38px;top:52px;text-align:right;color:var(--white);
  font-family:"Roboto Condensed",sans-serif;font-weight:700}
.identity .name{font-size:26px;line-height:30px}
.identity .role{font-size:20px;line-height:26px;letter-spacing:.5px}
.contacts{position:absolute;right:28px;top:158px;list-style:none;
  font-family:"Roboto Condensed",sans-serif;font-weight:700;font-size:16.5px;color:var(--white)}
.contacts li{display:flex;justify-content:flex-end;align-items:center;height:31.2px;gap:10px}
.contacts svg{width:20px;height:20px;flex:none}

/* back */
.card-back{left:104px;top:638px;width:745px;height:445px;background:var(--back-grey)}
.panel{position:absolute;background:var(--white)}
.panel-a{left:0;top:38px;width:341px;height:41px}
.panel-b{left:0;top:232px;width:376px;height:52px}
.panel-top{left:341px;top:0;width:404px;height:111px}
.panel-band{left:390px;top:117px;width:355px;height:46px}
.panel-c{left:411px;top:358px;width:334px;height:87px}

.say-block{position:absolute;left:14px;top:94px;display:flex;align-items:center;gap:8px}
.say-big{font-family:"Black Ops One",sans-serif;font-size:56px;line-height:54px;color:var(--ink);letter-spacing:3px}
.say-small{font-family:"Oswald",sans-serif;font-weight:500;font-size:25px;line-height:30px;color:var(--red);letter-spacing:6px}

.be-block{position:absolute;left:366px;top:10px;display:flex;align-items:flex-start}
.quote-open{font-family:"Playfair Display",serif;font-style:italic;font-weight:700;font-size:58px;line-height:60px;color:var(--red);margin-right:6px}
.be{font-family:"Archivo Black",sans-serif;font-size:102px;line-height:100px;color:var(--ink);letter-spacing:-6px}
.who{margin-left:8px;margin-top:16px;font-family:"Oswald",sans-serif;font-weight:500;color:var(--red);line-height:1}
.who .w1{display:block;font-size:46px}
.who .w2{display:block;font-size:31px;margin-top:-2px}

.stack{position:absolute;text-align:center;text-transform:uppercase}
.stack .red{font-family:"Federant",serif;color:var(--red);display:block}
.stack .dark{font-family:"Black Ops One",sans-serif;color:var(--ink);display:block}
.stack-right{left:411px;top:172px;width:300px}
.stack-right .red{font-size:42px;line-height:41px;letter-spacing:2px}
.stack-right .dark{font-size:37px;line-height:48px;margin-top:2px}
.stack-left{left:14px;top:302px;width:348px}
.stack-left .red{font-size:35px;line-height:40px;letter-spacing:2px}
.stack-left .dark{font-family:"Federant",serif;font-size:34px;line-height:44px;letter-spacing:3px}
.author{position:absolute;left:411px;top:386px;width:334px;text-align:center;
  font-family:"Playfair Display",serif;font-style:italic;font-weight:700;font-size:26px;color:var(--ink)}
</style>
</head>
<body>
<main class="canvas">

  <section class="card card-front" aria-label="Business card front">
    <svg class="front-shapes" viewBox="0 0 724 455" preserveAspectRatio="none" aria-hidden="true">
      <path d="M241 0 C300 120 262 330 84 455 L724 455 L724 0 Z" fill="#2c2c2c"/>
      <path d="M230 0 C284 125 236 335 52 455 L84 455 C262 330 300 120 241 0 Z" fill="#ea1f26"/>
    </svg>

    <div class="school-name"><span class="school-dot"></span><span class="line1">Pelbrook</span><span class="line2">Primary School</span></div>

    <div class="identity">
      <p class="name">Gareth Moffat</p>
      <p class="role">PRINCIPAL</p>
    </div>

    <ul class="contacts">
      <li>(08) 9371 2654
        <svg viewBox="0 0 20 20" fill="none" stroke="#fff" stroke-width="1.8"><path d="M5 2 L8 2 L9 6 L7 8 C8 11 9 12 12 13 L14 11 L18 12 L18 15 C18 17 16 18 14 17.5 C8 16 4 12 2.5 6 C2 4 3 2 5 2 Z"/></svg></li>
      <li>(08) 9371 5902
        <svg viewBox="0 0 20 20" fill="none" stroke="#fff" stroke-width="1.6"><rect x="5" y="2" width="10" height="6"/><rect x="2" y="8" width="16" height="7"/><rect x="5" y="13" width="10" height="5"/></svg></li>
      <li>0438 592 706
        <svg viewBox="0 0 20 20" fill="none" stroke="#fff" stroke-width="1.6"><rect x="5" y="1.5" width="10" height="17" rx="1.5"/><line x1="9" y1="16" x2="11" y2="16"/></svg></li>
      <li>Gareth.Moffat@learnmail-west.example
        <svg viewBox="0 0 20 20" fill="none" stroke="#fff" stroke-width="1.6"><rect x="2" y="4" width="16" height="12"/><path d="M2 4 L10 11 L18 4"/></svg></li>
      <li>117 Carrisfield Road HIGH WYCOMBE WA 6148
        <svg viewBox="0 0 20 20" fill="none" stroke="#fff" stroke-width="1.6"><path d="M2 9 L10 3 L18 9"/><rect x="4" y="9" width="12" height="8"/><rect x="8.5" y="12" width="3" height="5"/></svg></li>
      <li>www.pelbrookps.example.edu
        <svg viewBox="0 0 20 20" fill="none" stroke="#fff" stroke-width="1.5"><circle cx="10" cy="10" r="8"/><ellipse cx="10" cy="10" rx="3.5" ry="8"/><line x1="2" y1="10" x2="18" y2="10"/></svg></li>
      <li>au.proflink.example/in/garethmoffat/
        <svg viewBox="0 0 20 20" fill="none" stroke="#fff" stroke-width="1.6"><rect x="2.5" y="2.5" width="15" height="15" rx="2"/></svg></li>
    </ul>
  </section>

  <section class="card card-back" aria-label="Business card back with quote">
    <div class="panel panel-a"></div>
    <div class="panel panel-b"></div>
    <div class="panel panel-top"></div>
    <div class="panel panel-band"></div>
    <div class="panel panel-c"></div>

    <div class="be-block">
      <span class="quote-open">“</span>
      <span class="be">BE</span>
      <span class="who"><span class="w1">WHO</span><span class="w2">YOU ARE</span></span>
    </div>

    <div class="say-block">
      <div class="say-big">AND<br>SAY</div>
      <div class="say-small">WHAT<br>YOU<br>FEEL</div>
    </div>

    <p class="stack stack-right">
      <span class="red">Because</span>
      <span class="red">those</span>
      <span class="red">who mind</span>
      <span class="dark">Don’t matter</span>
    </p>

    <p class="stack stack-left">
      <span class="red">And those</span>
      <span class="red">who matter</span>
      <span class="dark">Don’t mind.”</span>
    </p>

    <p class="author">Dr. Plimm</p>
  </section>

</main>
</body>
</html>
```